17 Ways Your Nest Egg Can Bloom Book Cover

I need a book cover for a softcover book I will market directly.
The name of the book will be.
"17 Ways Your Nest Egg Can Bloom!"

I'm open to any and all ideas. But I want the book cover to stand out, to draw people's interest. But feel free to use your skill set to come up with good ideas.

I will be selling this book door to door and onine as well.

Target Market(s)

45-60 year old married couples

Industry/Entity Type

Financial Planning

Colors

Designer to choose colors to be used in the design.

Requirements
Must have
• website address.
• www.lanternoakadvisors.com
Nice to have
• like to have my picture on the back cover, with my company logo too if possible.

```html
<!DOCTYPE html>
<html lang="en">
<head>
<meta charset="utf-8">
<title>17 Ways Your Nest Egg Can Bloom – Book Cover</title>
<link rel="stylesheet" href="https://fonts.googleapis.com/css2?family=Cinzel:wght@500&family=Alfa+Slab+One&family=Lato:wght@700&family=EB+Garamond:wght@500&display=swap">
<style>
  :root {
    --cover-tan: #97786a;
    --ink: #080909;
    --pale: #d8dcdc;
  }
  html, body {
    margin: 0;
    padding: 0;
    overflow: hidden;
    background: var(--cover-tan);
  }
  .cover {
    position: relative;
    width: 750px;
    height: 1200px;
    overflow: hidden;
    background: var(--cover-tan);
  }
  .cover-art {
    position: absolute;
    inset: 0;
    display: block;
  }
  .numeral { font-family: "Alfa Slab One", serif; fill: var(--ink); }
  .title-line { font-family: "Cinzel", serif; font-weight: 500; fill: var(--pale); }
  .title-punch { font-family: "Alfa Slab One", serif; fill: var(--ink); }
  .author {
    position: absolute;
    top: 18px;
    left: 0;
    width: 750px;
    text-align: center;
    font-family: "Lato", sans-serif;
    font-weight: 700;
    font-size: 30px;
    letter-spacing: 1px;
    color: var(--pale);
    margin: 0;
  }
  .website {
    position: absolute;
    bottom: 16px;
    left: 0;
    width: 750px;
    text-align: center;
    font-family: "EB Garamond", serif;
    font-weight: 500;
    font-size: 27px;
    color: var(--ink);
    margin: 0;
  }
</style>
</head>
<body>
  <main class="cover">
    <svg class="cover-art" width="750" height="1200" viewBox="0 0 750 1200" aria-labelledby="book-title">
      <title id="book-title">17 Ways Your Nest Egg Can Bloom!</title>
      <defs>
        <linearGradient id="homes-tone" x1="0" y1="0" x2="0" y2="1">
          <stop offset="0" stop-color="#2a2320"/>
          <stop offset="1" stop-color="#7d6256"/>
        </linearGradient>
      </defs>

      <!-- oversized numeral behind the title -->
      <text class="numeral" x="0" y="478" font-size="600" textLength="740" lengthAdjust="spacingAndGlyphs">17</text>

      <!-- dark title band -->
      <rect class="title-band" x="0" y="464" width="750" height="120" fill="var(--ink)"/>

      <text class="title-line" x="18" y="364" font-size="108" textLength="712" lengthAdjust="spacingAndGlyphs">WAYS YOUR</text>
      <text class="title-line" x="38" y="452" font-size="92" textLength="692" lengthAdjust="spacingAndGlyphs">NEST EGG</text>
      <text class="title-line" x="375" y="565" font-size="120" text-anchor="middle">CAN</text>

      <text class="title-punch" x="16" y="780" font-size="230" textLength="718" lengthAdjust="spacingAndGlyphs">BLOOM!</text>

      <rect x="30" y="822" width="690" height="300" fill="url(#homes-tone)" role="img" aria-label="Illustration of two house silhouettes with rooftops and windows"/>
    </svg>

    <p class="author">EVAN MARSH</p>
    <p class="website">www.lanternoakadvisors.com</p>
  </main>
</body>
</html>
```